Business Card Design for a Handbags business

We are modernising our handbags website (see attached file for new front page) and are in need of a modern business card and a related design we can use on a small marquee at the markets, on letterhead, emails etc.

As the leather handbags we mostly import are from Italy, we want a smart modern European feel to the design. We are currently thinking about changing the name of the business from Meadowlark Handbags (see www.meadowlarkhandbags.com.au) to Vantera Handbags. Also open to other suggestions you may have that communicates the European influence and quality.

Target Market(s)

25-65 year old women (and some men)

Industry/Entity Type

Business

Contact Information for Business Card

Single or double sided - whichever creates more of an impact

Font styles to use
Serif
Sans Serif

Requirements
Must have
• Clean crisp look, slightly Italian or European look and feel to reflect where the handbags are imported from
Nice to have
• open to ideas

```html
<!DOCTYPE html>
<html lang="en">
<head>
<meta charset="utf-8">
<title>Luxury Leather Handbags – Business Card</title>
<link rel="stylesheet" href="https://fonts.googleapis.com/css2?family=Old+Standard+TT:wght@400;700&family=Open+Sans:wght@400;800&display=swap">
<style>
  :root {
    --page-bg: #e9e6e1;
    --card-white: #fbfbfa;
    --ink: #141414;
    --band-yellow: #e5e21f;
    --band-black: #111111;
    --panel-green: #cfe7c4;
    --panel-green-light: #e3f1dc;
    --photo-tone-a: #efe9e3;
    --photo-tone-b: #f8f6f3;
    --bag-tone-a: #8d7a6a;
    --bag-tone-b: #c9b8a6;
  }
  * { box-sizing: border-box; margin: 0; padding: 0; }
  html, body { width: 1200px; height: 902px; overflow: hidden; }
  body { background: var(--page-bg); position: relative; font-family: "Open Sans", sans-serif; }

  .card {
    position: absolute;
    width: 560px;
    height: 320px;
    overflow: hidden;
    box-shadow: 0 10px 28px rgba(0,0,0,0.22);
  }

  /* Front side */
  .card-front { left: 60px; top: 90px; background: var(--card-white); }
  .card-front .model-photo {
    position: absolute; left: 0; top: 0; width: 250px; height: 320px;
    background: linear-gradient(90deg, var(--photo-tone-a), var(--photo-tone-b) 80%, var(--card-white));
  }
  .card-front .brand-line {
    position: absolute; right: 40px; bottom: 62px;
    font-family: "Old Standard TT", serif; font-weight: 700;
    font-size: 46px; color: var(--ink); letter-spacing: -1px;
    transform: scaleX(0.78); transform-origin: right bottom;
    white-space: nowrap;
  }

  /* Back side */
  .card-back { left: 580px; top: 500px; background: var(--band-yellow); }
  .card-back .bands { position: absolute; inset: 0; }
  .card-back .holder-name {
    position: absolute; left: 30px; top: 26px;
    font-weight: 800; font-size: 15px; color: var(--ink); letter-spacing: 0.3px;
  }
  .card-back .product-photo {
    position: absolute; left: 52px; top: 80px; width: 225px; height: 180px;
    background: radial-gradient(circle at 50% 50%, var(--bag-tone-b), var(--bag-tone-a) 70%, #f3f3f3 100%);
  }
  .card-back .brand-block {
    position: absolute; left: 300px; top: 78px;
    font-family: "Old Standard TT", serif; font-size: 27px; line-height: 1.02; color: var(--ink);
  }
  .card-back .brand-block span { display: block; }
  .card-back .brand-block .second { padding-left: 18px; }
  .card-back .address {
    position: absolute; left: 318px; top: 178px;
    font-size: 11px; line-height: 1.5; letter-spacing: 1px; color: var(--ink);
  }
  .card-back .address .city { padding-left: 10px; }
  .card-back .phone {
    position: absolute; left: 348px; top: 234px;
    display: flex; align-items: center; gap: 8px;
    font-size: 12px; letter-spacing: 1px; color: var(--ink);
  }
</style>
</head>
<body>

<section class="card card-front">
  <div class="model-photo" role="img" aria-label="Faded photo of a woman holding a leather handbag"></div>
  <p class="brand-line">Luxury Leather Handbags</p>
</section>

<section class="card card-back">
  <svg class="bands" width="560" height="320" viewBox="0 0 560 320" aria-hidden="true">
    <path d="M300 0 H560 V38 H318 Q300 38 296 52 L290 62 H0 V0 Z" fill="var(--band-yellow)"/>
    <path d="M300 0 H560 V38 H318 Q304 38 300 26 Z" fill="var(--band-black)"/>
    <defs>
      <linearGradient id="panelFill" x1="0" y1="0" x2="1" y2="1">
        <stop offset="0" stop-color="var(--panel-green)"/>
        <stop offset="1" stop-color="var(--panel-green-light)"/>
      </linearGradient>
    </defs>
    <path d="M40 62 H290 L296 52 Q300 38 318 38 H560 V270 H40 Z" fill="url(#panelFill)"/>
    <rect x="0" y="270" width="560" height="12" fill="var(--band-yellow)"/>
    <rect x="0" y="282" width="560" height="38" fill="var(--band-black)"/>
  </svg>

  <p class="holder-name">CLARA VENN</p>
  <div class="product-photo" role="img" aria-label="Collage of assorted leather handbags"></div>

  <h1 class="brand-block"><span>Luxury Leather</span><span class="second">Handbags</span></h1>

  <p class="address">Kelmore<br><span class="city">Northvale</span></p>

  <p class="phone">
    <svg width="16" height="14" viewBox="0 0 16 14" aria-hidden="true">
      <rect x="0.5" y="0.5" width="15" height="13" rx="2" fill="var(--ink)"/>
      <path d="M4 5 Q8 2 12 5 L11 6.5 H5 Z" fill="var(--panel-green-light)"/>
      <rect x="5" y="7.5" width="6" height="3.5" rx="1" fill="var(--panel-green-light)"/>
    </svg>
    <span>0400 555 019</span>
  </p>
</section>

</body>
</html>
```